Design for a Service-Based Estimate

We want a design for an Estimate that will always be sent in PDF format. The estimate or proposal is a critical document that needs to plainly show the service items, item description but also needs to be attractive and professional looking. Our current estimate deliverable is attached but it looks really basic like a Word document

```html
<!DOCTYPE html>
<html lang="en">
<head>
<meta charset="utf-8">
<title>Estimate – Keystone Slab</title>
<link href="https://fonts.googleapis.com/css2?family=Open+Sans:wght@400;600;700;800&display=swap" rel="stylesheet">
<style>
  :root{
    --navy:#23245f;
    --red:#d23a26;
    --ink:#2a2a2a;
    --muted:#777;
    --rule:#cfcfcf;
    --bg:#e9e9ec;
    --paper:#ffffff;
  }
  *{box-sizing:border-box;margin:0;padding:0}
  html,body{width:1200px;height:1200px;overflow:hidden;background:var(--bg);font-family:"Open Sans",sans-serif;color:var(--ink)}
  .page{position:absolute;left:187px;top:50px;width:825px;height:1100px;background:var(--paper);box-shadow:0 6px 24px rgba(0,0,0,.12);overflow:hidden}
  .brand{position:absolute;left:60px;top:70px;display:flex;align-items:center;gap:10px}
  .brand-mark{width:18px;height:18px;background:var(--navy)}
  .brand-name{font-weight:800;font-size:30px;letter-spacing:1px;color:var(--navy)}
  .contact{position:absolute;right:60px;top:60px;list-style:none;font-size:11px;line-height:20px}
  .contact li{display:flex;align-items:center;gap:8px}
  .contact .dot{width:14px;height:14px;border-radius:50%;background:var(--red);display:inline-flex;align-items:center;justify-content:center}
  .bid{position:absolute;right:60px;top:150px;font-size:11px;line-height:17px;text-align:left}
  .bid b{font-weight:700}
  .bid .label{color:var(--red);font-weight:700}
  .client{position:absolute;left:60px;top:165px;font-size:11px;line-height:16px}
  .client .to{color:var(--muted)}
  .client .name{font-weight:700;font-size:14px;line-height:20px}
  .client .label{color:var(--red);font-weight:700}
  .estimate{position:absolute;left:60px;top:250px;width:705px;border-collapse:collapse;font-size:11.5px}
  .estimate th{background:var(--navy);color:#fff;font-weight:600;text-align:left;padding:9px 12px;font-size:12px}
  .estimate td{padding:14px 12px;vertical-align:top;line-height:18px;border-bottom:1px solid var(--rule)}
  .estimate .num{text-align:right}
  .estimate .tag{color:var(--red);font-weight:700}
  .estimate .total td{border-bottom:1px solid var(--rule);font-weight:600}
  .col-item{width:44%}
  .terms{position:absolute;left:60px;top:640px;width:705px}
  .terms h2{font-size:18px;font-weight:600;margin-bottom:12px}
  .terms ol{padding-left:22px;font-size:11.5px;line-height:24px}
  .terms li{padding-left:8px}
  .footer{position:absolute;left:0;bottom:0;width:825px;height:230px}
  .licenses{position:absolute;left:40px;bottom:38px;color:#fff;font-size:14px;line-height:22px;font-weight:600}
</style>
</head>
<body>
<main class="page">
  <div class="brand"><span class="brand-mark"></span><span class="brand-name">KEYSTONE SLAB</span></div>

  <ul class="contact">
    <li><span class="dot"><svg width="8" height="8" viewBox="0 0 8 8"><path d="M1.5 1 L3 1 L3.5 2.6 L2.6 3.3 Q3.4 4.8 4.8 5.5 L5.5 4.6 L7 5.1 L7 6.6 Q3.5 7 1 2.5 Z" fill="#fff"/></svg></span>(555) 014-2270</li>
    <li><span class="dot"><svg width="8" height="8" viewBox="0 0 8 8"><rect x="1" y="2" width="6" height="4" fill="none" stroke="#fff"/><path d="M1 2 L4 4.5 L7 2" fill="none" stroke="#fff"/></svg></span>hello@keystoneslab.com</li>
    <li><span class="dot"><svg width="8" height="8" viewBox="0 0 8 8"><circle cx="4" cy="4" r="3" fill="none" stroke="#fff"/><path d="M1 4 H7 M4 1 V7" stroke="#fff" stroke-width=".8"/></svg></span>www.keystoneslab.com</li>
  </ul>

  <div class="bid"><b>Bid# 01245</b><br><span class="label">Date:</span> 14th January, 2021</div>

  <div class="client">
    <div class="to">To</div>
    <div class="name">Dana Whitlock</div>
    <div>48 Harbor Lane, Fairview 30210</div>
    <div><span class="label">E:</span> dwhitlock@mailbox.com</div>
  </div>

  <table class="estimate">
    <thead>
      <tr><th class="col-item">Item</th><th>Quantity</th><th>U/M</th><th>Unit Rate</th><th class="num">Amount</th></tr>
    </thead>
    <tbody>
      <tr>
        <td>Form, Pour &amp; Finish New Concrete Slab (24' x 24' x 4"),<br><span class="tag">Includes:</span><br>3000 psi Concrete Mix, Footer (12" X 8") with One (#5)<br>Continuous Rebar, Wire mesh Reinforcement and<br>Saw-Cut Expansion Joints</td>
        <td>576</td><td>S/F</td><td>$8.65</td><td class="num">$ 4,982.40</td>
      </tr>
      <tr>
        <td><span class="tag">Optional:</span><br>Add (2' X 24' X 4") Small Ramp Area)</td>
        <td>48</td><td>S/F</td><td>$8.65</td><td class="num">$ 415.20</td>
      </tr>
      <tr class="total">
        <td></td><td></td><td></td><td>Total Amount</td><td class="num">$ 5,397.60</td>
      </tr>
    </tbody>
  </table>

  <section class="terms">
    <h2>Terms &amp; Conditions</h2>
    <ol>
      <li>Prices as quoted in this estimate are valid for 60days only.</li>
      <li>Payment in full, lesss any previously paid amounts, is due to teh Contractor upon completion of the proposed scope of work.</li>
      <li>All Chnage order requests must be communicated in writing to the Contractor by the Clinet or their authorized representaive.</li>
      <li>All measurments listed in this estimate are approximate and may vary slightly due to actual field conditions.</li>
    </ol>
  </section>

  <footer class="footer">
    <svg width="825" height="230" viewBox="0 0 825 230">
      <polygon points="330,40 825,40 825,62 310,62" fill="var(--navy)"/>
      <polygon points="300,70 825,70 825,74 297,74" fill="var(--red)"/>
      <polygon points="0,92 300,92 292,102 0,102" fill="var(--navy)"/>
      <polygon points="0,108 288,108 285,112 0,112" fill="var(--red)"/>
      <polygon points="0,118 390,118 470,230 0,230" fill="var(--red)"/>
    </svg>
    <div class="licenses">Lee (LIC00-10482, LIC00-20935) &nbsp;|&nbsp; Collier (LCC00-4417)<br>Cape Coral (#10274) &nbsp;|&nbsp; Charlotte (AAA-00-55031)</div>
  </footer>
</main>
</body>
</html>
```